Banner Design for High End Jewelry Website

We need a banner for our website (brindlestone.com) for a sale that we will be running. The banner should be a size 1187 × 400. I have included a few pieces of jewelry to be included in the banner (do not need to use all, can use just some). The banner should say:
"Christmas is Closer Than You Think Sale!"
Shop Now

Industry/Entity Type

Jewelry

```html
<!DOCTYPE html>
<html lang="en">
<head>
<meta charset="utf-8">
<title>Brindlestone – Christmas Sale Banner Concepts</title>
<link href="https://fonts.googleapis.com/css2?family=Cormorant+Garamond:wght@500;600;700&family=Open+Sans:wght@400;600&display=swap" rel="stylesheet">
<style>
  :root {
    --stage-light: #f7f7f7;
    --stage-dark: #e3e3e3;
    --page: #ffffff;
    --sale-pink: #e5126a;
    --ink: #1c1c1c;
    --muted: #8a8a8a;
    --nav-brown: #9a8473;
    --nav-line: #b9a898;
    --band-beige: #d6c6b4;
    --corner-gold: #ecd3a0;
    --frost-top: #e9dde2;
    --frost-mid: #dfe3ec;
    --frost-low: #c9d4e6;
    --gold-soft: #e2bf5c;
    --gold-fade: rgba(226, 191, 92, 0);
  }
  * { box-sizing: border-box; margin: 0; padding: 0; }
  html, body { width: 1200px; height: 736px; overflow: hidden; }
  body {
    position: relative;
    background: radial-gradient(ellipse at 50% 35%, var(--stage-light) 0%, var(--stage-dark) 100%);
    font-family: "Open Sans", Arial, sans-serif;
  }

  .concept {
    position: absolute;
    top: 137px;
    width: 558px;
    height: 459px;
    background: var(--page);
    overflow: hidden;
  }
  .concept--long-title { left: 34px; }
  .concept--short-title { left: 608px; }

  .banner { position: absolute; overflow: hidden; }
  .banner--hero { left: 0; top: 0; width: 558px; height: 188px; }
  .banner--inline { left: 73px; top: 277px; width: 413px; height: 139px; }

  .banner__backdrop {
    position: absolute; inset: 0;
    background:
      radial-gradient(ellipse at 50% 75%, rgba(255,255,255,0.85) 0%, rgba(255,255,255,0) 55%),
      linear-gradient(180deg, var(--frost-top) 0%, var(--frost-mid) 50%, var(--frost-low) 100%);
  }
  .banner__product {
    position: absolute;
    border-radius: 50%;
    background: radial-gradient(ellipse at 50% 50%, var(--gold-soft) 0%, var(--gold-soft) 45%, var(--gold-fade) 72%);
  }
  .banner--hero .banner__product--left { left: 18px; top: 42px; width: 108px; height: 104px; }
  .banner--hero .banner__product--right { left: 430px; top: 44px; width: 108px; height: 100px; }
  .banner--inline .banner__product--left { left: 12px; top: 34px; width: 80px; height: 76px; }
  .banner--inline .banner__product--right { left: 322px; top: 12px; width: 80px; height: 96px; }

  .banner__copy {
    position: absolute;
    text-align: center;
    color: var(--sale-pink);
    font-family: "Cormorant Garamond", Georgia, serif;
    font-weight: 600;
    white-space: nowrap;
  }
  .banner--hero .banner__copy { left: 120px; width: 310px; }
  .banner--inline .banner__copy { left: 85px; width: 240px; }

  .banner--hero .banner__title--stacked { font-size: 31px; line-height: 31px; }
  .banner--inline .banner__title--stacked { font-size: 23.5px; line-height: 23px; }
  .banner--hero .banner__copy--stacked { top: 63px; }
  .banner--inline .banner__copy--stacked { top: 47px; }

  .banner__title--caps { letter-spacing: 0.5px; }
  .banner--hero .banner__title--caps { font-size: 31px; line-height: 1; }
  .banner--inline .banner__title--caps { font-size: 23px; line-height: 1; }
  .banner--hero .banner__subtitle { font-size: 19px; line-height: 1; margin-top: 4px; }
  .banner--inline .banner__subtitle { font-size: 15px; line-height: 1; margin-top: 2px; }
  .banner--hero .banner__copy--caps { top: 73px; }
  .banner--inline .banner__copy--caps { top: 53px; }

  .utility-bar {
    position: absolute; top: 193px; left: 270px;
    display: flex; gap: 20px;
    font-size: 6px; letter-spacing: 0.3px; color: var(--muted);
  }
  .utility-bar__item { display: flex; align-items: center; gap: 5px; }
  .utility-bar__item svg { width: 8px; height: 8px; }

  .signup-corner {
    position: absolute; right: 0; top: 188px;
    width: 0; height: 0;
    border-top: 46px solid var(--corner-gold);
    border-left: 46px solid transparent;
  }
  .signup-corner__label {
    position: absolute; right: 2px; top: 200px;
    font-size: 6px; color: #5a4a3a;
    transform: rotate(45deg);
  }

  .brand { position: absolute; left: 73px; top: 209px; width: 150px; }
  .brand__name {
    font-family: "Cormorant Garamond", Georgia, serif;
    font-weight: 500; font-size: 28px; line-height: 1; color: var(--ink);
  }
  .brand__tagline {
    margin-top: 11px; font-size: 7.2px; color: var(--ink); white-space: nowrap;
  }

  .search {
    position: absolute; left: 253px; top: 216px; width: 118px; height: 11px;
    border-bottom: 1px solid #cfcfcf;
    display: flex; align-items: center; font-size: 5px; color: var(--muted);
  }
  .search svg { width: 6px; height: 6px; margin: 0 5px 0 4px; }
  .search__submit {
    position: absolute; right: 0; top: 0; width: 11px; height: 11px;
    background: var(--nav-brown); display: flex; align-items: center; justify-content: center;
  }
  .search__submit svg { width: 7px; height: 7px; margin: 0; }

  .account-links {
    position: absolute; left: 387px; top: 210px;
    display: flex; gap: 10px;
    font-size: 4.8px; color: var(--muted); text-align: center;
  }
  .account-links__item { display: flex; flex-direction: column; align-items: center; gap: 3px; }
  .account-links__item svg { width: 10px; height: 9px; }

  .main-nav {
    position: absolute; left: 218px; top: 240px; height: 17px;
    display: flex; background: var(--nav-brown);
  }
  .main-nav__item {
    color: #fff; font-size: 6.3px; letter-spacing: 0.3px;
    padding: 0 9px; line-height: 17px; border-right: 1px solid var(--nav-line);
  }
  .main-nav__item:last-child { border-right: 0; }

  .section-band {
    position: absolute; left: 73px; top: 432px; width: 413px; height: 21px;
    background: var(--band-beige);
    color: #fff; font-size: 9px; letter-spacing: 0.4px;
    text-align: center; line-height: 21px;
  }
  .section-band__action {
    position: absolute; right: 4px; top: 4px; height: 13px; padding: 0 5px;
    background: var(--nav-brown); font-size: 4.8px; line-height: 13px;
  }
  .section-body {
    position: absolute; left: 73px; top: 453px; width: 413px; height: 10px;
    border-left: 1px solid #e6e0d8; border-right: 1px solid #e6e0d8;
  }
</style>
</head>
<body>

<section class="concept concept--long-title">
  <div class="banner banner--hero">
    <div class="banner__backdrop" role="img" aria-label="Soft snowy winter scene with blurred evergreen trees and falling snow"></div>
    <div class="banner__product banner__product--left" role="img" aria-label="Photo of a gold scaled dome ring with diamonds"></div>
    <div class="banner__copy banner__copy--stacked"><p class="banner__title banner__title--stacked">Christmas is Closer<br>Than You Think Sale!</p></div>
    <div class="banner__product banner__product--right" role="img" aria-label="Photo of a gold ring with coloured cabochon stones"></div>
  </div>

  <div class="utility-bar">
    <span class="utility-bar__item"><svg viewBox="0 0 10 10"><path d="M2 1l2 2-1 1.3a6 6 0 0 0 2.7 2.7L7 6l2 2-1.3 1.3C4.5 9 1 5.5.7 2.3z" fill="none" stroke="#8a8a8a" stroke-width=".8"/></svg>800 - 555 - 0142</span>
    <span class="utility-bar__item"><svg viewBox="0 0 10 10"><path d="M1 4l2-2.5h4L9 4 5 9z M1 4h8" fill="none" stroke="#8a8a8a" stroke-width=".8"/></svg>SELL JEWELRY</span>
    <span class="utility-bar__item"><svg viewBox="0 0 10 10"><circle cx="5" cy="3.2" r="2.2" fill="none" stroke="#8a8a8a" stroke-width=".8"/><path d="M1 9.5c.5-2.5 2-3.5 4-3.5s3.5 1 4 3.5" fill="none" stroke="#8a8a8a" stroke-width=".8"/></svg>SIGN IN / REGISTER</span>
  </div>
  <div class="signup-corner"></div>
  <span class="signup-corner__label">Sign up!</span>

  <div class="brand">
    <p class="brand__name">Brindlestone</p>
    <p class="brand__tagline">FINE ESTATE AND DESIGNER JEWELRY</p>
  </div>

  <div class="search">
    <svg viewBox="0 0 10 10"><circle cx="4" cy="4" r="3" fill="none" stroke="#8a8a8a"/><path d="M6.2 6.2L9 9" stroke="#8a8a8a"/></svg>Search
    <span class="search__submit"><svg viewBox="0 0 10 10"><path d="M2 5l2 2 4-4" fill="none" stroke="#fff" stroke-width="1.4"/></svg></span>
  </div>

  <div class="account-links">
    <span class="account-links__item"><svg viewBox="0 0 12 10"><rect x="1" y="1.5" width="10" height="7" fill="none" stroke="#9a8473" stroke-width=".8"/><path d="M1 1.5l5 4 5-4" fill="none" stroke="#9a8473" stroke-width=".8"/></svg>NEWSLETTER</span>
    <span class="account-links__item"><svg viewBox="0 0 12 10"><path d="M6 9L1.5 4.5a2.3 2.3 0 0 1 4.5-2.3 2.3 2.3 0 0 1 4.5 2.3z" fill="none" stroke="#9a8473" stroke-width=".8"/></svg>WISHLIST</span>
    <span class="account-links__item"><svg viewBox="0 0 12 10"><path d="M1 1h2l1.5 5.5h5L11 3H4" fill="none" stroke="#9a8473" stroke-width=".8"/><circle cx="5" cy="8.5" r=".8" fill="#9a8473"/><circle cx="9" cy="8.5" r=".8" fill="#9a8473"/></svg>CART (0)</span>
  </div>

  <nav class="main-nav">
    <span class="main-nav__item">FINE JEWELRY</span>
    <span class="main-nav__item">TIMEPIECES</span>
    <span class="main-nav__item">ACCESSORIES</span>
    <span class="main-nav__item">DESIGNERS</span>
    <span class="main-nav__item">SALE</span>
  </nav>

  <div class="banner banner--inline">
    <div class="banner__backdrop" role="img" aria-label="Soft snowy winter scene with blurred evergreen trees and falling snow"></div>
    <div class="banner__product banner__product--left" role="img" aria-label="Photo of a gold scaled dome ring with diamonds"></div>
    <div class="banner__copy banner__copy--stacked"><p class="banner__title banner__title--stacked">Christmas is Closer<br>Than You Think Sale!</p></div>
    <div class="banner__product banner__product--right" role="img" aria-label="Photo of a gold ring with coloured cabochon stones"></div>
  </div>

  <div class="section-band">NEW ARRIVALS<span class="section-band__action">VIEW ALL</span></div>
  <div class="section-body"></div>
</section>

<section class="concept concept--short-title">
  <div class="banner banner--hero">
    <div class="banner__backdrop" role="img" aria-label="Soft snowy winter scene with blurred evergreen trees and falling snow"></div>
    <div class="banner__product banner__product--left" role="img" aria-label="Photo of a gold scaled dome ring with diamonds"></div>
    <div class="banner__copy banner__copy--caps">
      <p class="banner__title banner__title--caps">CHRISTMAS SALE</p>
      <p class="banner__subtitle">It’s closer than you think.</p>
    </div>
    <div class="banner__product banner__product--right" role="img" aria-label="Photo of a gold ring with coloured cabochon stones"></div>
  </div>

  <div class="utility-bar">
    <span class="utility-bar__item"><svg viewBox="0 0 10 10"><path d="M2 1l2 2-1 1.3a6 6 0 0 0 2.7 2.7L7 6l2 2-1.3 1.3C4.5 9 1 5.5.7 2.3z" fill="none" stroke="#8a8a8a" stroke-width=".8"/></svg>800 - 555 - 0142</span>
    <span class="utility-bar__item"><svg viewBox="0 0 10 10"><path d="M1 4l2-2.5h4L9 4 5 9z M1 4h8" fill="none" stroke="#8a8a8a" stroke-width=".8"/></svg>SELL JEWELRY</span>
    <span class="utility-bar__item"><svg viewBox="0 0 10 10"><circle cx="5" cy="3.2" r="2.2" fill="none" stroke="#8a8a8a" stroke-width=".8"/><path d="M1 9.5c.5-2.5 2-3.5 4-3.5s3.5 1 4 3.5" fill="none" stroke="#8a8a8a" stroke-width=".8"/></svg>SIGN IN / REGISTER</span>
  </div>
  <div class="signup-corner"></div>
  <span class="signup-corner__label">Sign up!</span>

  <div class="brand">
    <p class="brand__name">Brindlestone</p>
    <p class="brand__tagline">FINE ESTATE AND DESIGNER JEWELRY</p>
  </div>

  <div class="search">
    <svg viewBox="0 0 10 10"><circle cx="4" cy="4" r="3" fill="none" stroke="#8a8a8a"/><path d="M6.2 6.2L9 9" stroke="#8a8a8a"/></svg>Search
    <span class="search__submit"><svg viewBox="0 0 10 10"><path d="M2 5l2 2 4-4" fill="none" stroke="#fff" stroke-width="1.4"/></svg></span>
  </div>

  <div class="account-links">
    <span class="account-links__item"><svg viewBox="0 0 12 10"><rect x="1" y="1.5" width="10" height="7" fill="none" stroke="#9a8473" stroke-width=".8"/><path d="M1 1.5l5 4 5-4" fill="none" stroke="#9a8473" stroke-width=".8"/></svg>NEWSLETTER</span>
    <span class="account-links__item"><svg viewBox="0 0 12 10"><path d="M6 9L1.5 4.5a2.3 2.3 0 0 1 4.5-2.3 2.3 2.3 0 0 1 4.5 2.3z" fill="none" stroke="#9a8473" stroke-width=".8"/></svg>WISHLIST</span>
    <span class="account-links__item"><svg viewBox="0 0 12 10"><path d="M1 1h2l1.5 5.5h5L11 3H4" fill="none" stroke="#9a8473" stroke-width=".8"/><circle cx="5" cy="8.5" r=".8" fill="#9a8473"/><circle cx="9" cy="8.5" r=".8" fill="#9a8473"/></svg>CART (0)</span>
  </div>

  <nav class="main-nav">
    <span class="main-nav__item">FINE JEWELRY</span>
    <span class="main-nav__item">TIMEPIECES</span>
    <span class="main-nav__item">ACCESSORIES</span>
    <span class="main-nav__item">DESIGNERS</span>
    <span class="main-nav__item">SALE</span>
  </nav>

  <div class="banner banner--inline">
    <div class="banner__backdrop" role="img" aria-label="Soft snowy winter scene with blurred evergreen trees and falling snow"></div>
    <div class="banner__product banner__product--left" role="img" aria-label="Photo of a gold scaled dome ring with diamonds"></div>
    <div class="banner__copy banner__copy--caps">
      <p class="banner__title banner__title--caps">CHRISTMAS SALE</p>
      <p class="banner__subtitle">It’s closer than you think.</p>
    </div>
    <div class="banner__product banner__product--right" role="img" aria-label="Photo of a gold ring with coloured cabochon stones"></div>
  </div>

  <div class="section-band">NEW ARRIVALS<span class="section-band__action">VIEW ALL</span></div>
  <div class="section-body"></div>
</section>

</body>
</html>
```